Brisk Framing website

I need a website for my construction. I want customers to see past builds and current projects Something that stands out and reflects awareness, safety, attention to details. I already have a logo designed by Pixel Harbor
Target Market(s)
Residential and Commercial sectors
Industry/Entity Type
Construction
Logo Text
Brisk Framing
Colors
EB3D1F
EC4F4E
F09395
F8D3D4
FCEDEE
Requirements
Must have
- My contact info
Nice to have
- Past projects

```html
<!DOCTYPE html>
<html lang="en">
<head>
<meta charset="utf-8">
<title>Brisk Framing</title>
<link rel="stylesheet" href="https://fonts.googleapis.com/css2?family=Arimo:wght@400;700&display=swap">
<style>
:root{
  --red:#eb3d1f;
  --red-soft:#ec4f4e;
  --pink:#f09395;
  --blush:#f8d3d4;
  --ink:#1a1a1a;
  --dark:#222222;
  --grey:#f3f3f3;
  --text:#333333;
  --white:#ffffff;
}
*{margin:0;padding:0;box-sizing:border-box}
html,body{width:1200px;height:4386px;overflow:hidden}
body{position:relative;font-family:"Arimo",Arial,sans-serif;color:var(--text);background:var(--white)}
.abs{position:absolute}
.btn{position:absolute;display:flex;align-items:center;justify-content:center;font-size:10px;font-weight:700;color:var(--white);text-transform:uppercase;clip-path:polygon(12% 0,100% 0,88% 100%,0 100%)}
.btn-red{background:var(--red)}
.btn-dark{background:var(--ink)}
.eyebrow{position:absolute;font-size:10px;letter-spacing:4px;text-transform:uppercase}
.section-title{position:absolute;left:0;width:1200px;text-align:center;font-size:52px;font-weight:400}
.chevron{position:absolute;left:585px;width:30px;height:22px}
.ph{position:absolute}

/* header */
.site-header{position:absolute;left:0;top:0;width:1200px;height:73px;background:var(--white)}
.brand{position:absolute;display:flex;align-items:center;gap:8px;font-weight:700;color:var(--red)}
.brand-mark{width:14px;height:14px;background:var(--red)}
.main-nav a{position:absolute;top:32px;font-size:10px;color:var(--ink);text-decoration:none;text-transform:uppercase}
.main-nav .active::after{content:"";position:absolute;left:0;right:0;top:21px;height:3px;background:var(--red)}
.phone-tab{position:absolute;left:902px;top:0;width:198px;height:34px;background:var(--red);color:var(--white);font-size:19px;display:flex;align-items:center;justify-content:flex-end;padding-right:14px;clip-path:polygon(10% 0,100% 0,100% 100%,0 100%)}
.phone-tab svg{position:absolute;left:26px;top:9px}
.social span{position:absolute;width:11px;height:11px;border-radius:50%}

/* hero + current */
.hero-photo{left:0;top:73px;width:1200px;height:700px;background:linear-gradient(160deg,#5a5550 0%,#3a3734 45%,#262626 100%)}
.hero-eyebrow{left:99px;top:241px;color:var(--white);font-size:12px;letter-spacing:5px}
.hero-title{position:absolute;left:99px;top:266px;font-size:52px;line-height:56px;color:var(--white);font-weight:400}
.quote-box{position:absolute;left:795px;top:511px;width:305px;height:122px;background:var(--red);text-align:center;color:var(--white)}
.quote-box h2{font-size:25px;font-weight:400;margin-top:24px}
.project-card{position:absolute;top:844px;width:305px;height:390px;background:var(--white);text-align:center}
.project-card .ph{left:0;top:0;width:305px;height:228px}
.project-card .pin{position:absolute;left:146px;top:228px;width:0;height:0;border-left:7px solid transparent;border-right:7px solid transparent;border-top:9px solid var(--red)}
.project-card h3{position:absolute;top:264px;width:100%;font-size:22px;font-weight:400;color:var(--ink)}
.project-card p{position:absolute;top:294px;left:32px;right:32px;font-size:10px;line-height:17px;color:var(--text)}

/* welcome */
.welcome-title{position:absolute;left:102px;top:1463px;font-size:50px;line-height:48px;font-weight:400;color:var(--ink)}
.welcome-rule{position:absolute;left:102px;top:1583px;width:68px;height:2px;background:var(--red)}
.welcome-copy{position:absolute;left:102px;width:430px;font-size:10.5px;line-height:17px}
.call-line{position:absolute;left:102px;top:1768px;display:flex;align-items:center;gap:10px;font-size:9px;font-weight:700;color:var(--ink)}
.call-line strong{font-size:22px;font-weight:400}

/* recent */
.recent{left:0;top:1954px;width:1200px;height:519px;background:var(--red)}
.recent-item{position:absolute;top:2153px;width:229px;text-align:center;color:var(--white);font-size:16px}
.recent-item .ph{position:relative;width:229px;height:170px}
.recent-item span{display:block;margin-top:18px}

/* services */
.service{position:absolute;top:2689px;width:220px}
.service h3{margin-top:18px;font-size:22px;font-weight:400;color:var(--ink)}
.service p{margin-top:12px;font-size:10px;line-height:17px}

/* testimonials */
.testimonials{left:0;top:2975px;width:1200px;height:324px;background:linear-gradient(90deg,#e3e3e3,#f6f6f6 60%,#ececec)}
.testimonial{position:absolute;top:3036px;width:480px;height:204px;background:var(--white);text-align:center;font-size:10px;line-height:17px}
.testimonial .qm{margin-top:32px;color:var(--red);font-size:34px;font-weight:700;line-height:20px;font-style:italic}
.testimonial .stars{margin-top:12px;color:#f2a33a;font-size:13px;letter-spacing:9px}
.testimonial p{margin:4px 72px 0}
.testimonial .who{margin-top:18px}

/* contact */
.contact-card{position:absolute;left:150px;top:3411px;width:900px;height:422px;background:var(--white)}
.field{position:absolute;background:var(--grey);border:1px solid #e6e6e6;font-size:9px;color:#777;padding:9px 16px}
.info{position:absolute;top:3866px;width:240px;text-align:center;color:var(--white)}
.info .tag{width:46px;height:26px;margin:0 auto;background:var(--ink);clip-path:polygon(18% 0,100% 0,82% 100%,0 100%);display:flex;align-items:center;justify-content:center}
.info small{display:block;margin-top:6px;font-size:8px;color:var(--blush)}
.info span{display:block;margin-top:2px;font-size:10px}

/* footer */
.footer-nav{position:absolute;left:0;top:4272px;width:1200px;height:82px;background:var(--white)}
.footer-nav a{position:absolute;top:36px;font-size:10px;font-weight:700;color:var(--ink);text-decoration:none}
.copyright{position:absolute;left:0;top:4354px;width:1200px;height:32px;background:var(--red);color:var(--white);font-size:9px;text-align:center;line-height:32px}
</style>
</head>
<body>

<header class="site-header">
  <div class="brand" style="left:85px;top:20px;font-size:24px"><span class="brand-mark"></span>Brisk Framing</div>
  <nav class="main-nav">
    <a class="active" style="left:414px">Home</a>
    <a style="left:487px">About</a>
    <a style="left:567px">Services</a>
    <a style="left:662px">Projects</a>
    <a style="left:759px">Contact Us</a>
  </nav>
  <div class="phone-tab">
    <svg width="16" height="16" viewBox="0 0 24 24" fill="none" stroke="#1a1a1a" stroke-width="2"><path d="M5 3h4l2 5-3 2a12 12 0 0 0 6 6l2-3 5 2v4a2 2 0 0 1-2 2A17 17 0 0 1 3 5a2 2 0 0 1 2-2z"/></svg>
    204-555-0193
  </div>
  <div class="social">
    <span style="left:966px;top:48px;background:var(--ink)"></span>
    <span style="left:1000px;top:48px;background:#bbb"></span>
    <span style="left:1037px;top:48px;background:#bbb"></span>
  </div>
</header>

<div class="ph hero-photo" role="img" aria-label="Photo of a construction worker levelling fresh concrete on a site"></div>
<svg class="abs" style="left:0;top:773px" width="1200" height="602" viewBox="0 773 1200 602">
  <polygon points="0,773 1200,773 1200,1268 1030,1375 0,1268" fill="#262626"/>
</svg>
<div class="eyebrow hero-eyebrow">Residential • Commercial</div>
<h1 class="hero-title">Lorem ipsum dolor<br>consectetuer adipiscing.</h1>
<a class="btn btn-red" style="left:102px;top:413px;width:141px;height:31px">Contact Us</a>
<div class="quote-box">
  <h2>Request a Quote</h2>
  <a class="btn btn-dark" style="left:80px;top:66px;width:145px;height:31px">Contact Us</a>
</div>

<svg class="chevron" style="top:700px" viewBox="0 0 30 22"><polygon points="0,0 30,0 15,22" fill="var(--red)"/><polyline points="9,6 15,12 21,6" fill="none" stroke="#262626" stroke-width="2"/></svg>
<div class="eyebrow" style="left:0;width:1200px;text-align:center;top:746px;color:#ccc">Brisk Framing</div>
<h2 class="section-title" style="top:760px;color:var(--white)">Current Projects</h2>

<article class="project-card" style="left:100px">
  <div class="ph" role="img" aria-label="Photo of scaffolding around a building under construction" style="background:linear-gradient(180deg,#b9c6d3,#8a7a66)"></div>
  <span class="pin"></span>
  <h3>Laoreet Dolore</h3>
  <p>Nostrud exerci tation ullamcorper suscipit lobortis nisl ut aliquip ex ea commodo consequat.</p>
  <a class="btn btn-red" style="left:78px;top:337px;width:148px;height:31px">Learn More</a>
</article>
<article class="project-card" style="left:448px">
  <div class="ph" role="img" aria-label="Aerial photo of workers tying rebar on a concrete deck" style="background:linear-gradient(135deg,#8e9aa0,#5f6b70)"></div>
  <span class="pin"></span>
  <h3>Euismod Tincidunt</h3>
  <p>Vel eum iriure dolor in hendrerit in vulputate velit esse molestie consequat vel illum dolore.</p>
  <a class="btn btn-red" style="left:78px;top:337px;width:148px;height:31px">Learn More</a>
</article>
<article class="project-card" style="left:795px">
  <div class="ph" role="img" aria-label="Photo of a multi-storey timber frame against blue sky" style="background:linear-gradient(180deg,#9cc3e0,#a77a55)"></div>
  <span class="pin"></span>
  <h3>Wisi Enim Ad Minim</h3>
  <p>Odio dignissim qui blandit praesent luptatum zzril augue duis dolore nulla facilisi.</p>
  <a class="btn btn-red" style="left:78px;top:337px;width:148px;height:31px">Learn More</a>
</article>

<div class="eyebrow" style="left:102px;top:1430px;color:#555">Welcome</div>
<h2 class="welcome-title">Brisk<br>Framing</h2>
<span class="welcome-rule"></span>
<p class="welcome-copy" style="top:1612px">Lorem ipsum dolor sit amet, consectetuer adipiscing elit, sed diam nonummy nibh euismod tincidunt ut laoreet dolore magna aliquam erat volutpat.</p>
<p class="welcome-copy" style="top:1663px">Ut wisi enim ad minim veniam, quis nostrud exerci tation ullamcorper suscipit lobortis nisl ut aliquip ex ea commodo consequat. Duis autem vel eum iriure dolor in hendrerit in vulputate velit esse molestie consequat, vel illum dolore eu feugiat nulla facilisis at vero eros et accumsan et iusto odio dignissim qui blandit praesent luptatum zzril delenit augue duis dolore te feugait nulla facilisi.</p>
<div class="call-line">Call us at:
  <svg width="24" height="24" viewBox="0 0 24 24" fill="none" stroke="var(--red)" stroke-width="1.6"><path d="M5 3h4l2 5-3 2a12 12 0 0 0 6 6l2-3 5 2v4a2 2 0 0 1-2 2A17 17 0 0 1 3 5a2 2 0 0 1 2-2z"/></svg>
  <strong>204-555-0193</strong></div>
<a class="btn btn-red" style="left:102px;top:1823px;width:145px;height:33px">Read More</a>
<a class="btn btn-dark" style="left:237px;top:1823px;width:145px;height:33px">Contact Us</a>

<svg class="abs" style="left:720px;top:1433px" width="245" height="80" viewBox="0 0 245 80"><polygon points="0,0 242,0 232,14 30,14 58,80 50,80" fill="var(--red)"/></svg>
<div class="ph" role="img" aria-label="Photo of a hard hat beside workers on a building site" style="left:616px;top:1469px;width:484px;height:395px;background:linear-gradient(160deg,#d9c79a,#a8926a 55%,#7e8a78)"></div>

<div class="abs recent"></div>
<svg class="chevron" style="top:2014px" viewBox="0 0 30 22"><polygon points="0,0 30,0 15,22" fill="var(--ink)"/><polyline points="9,6 15,12 21,6" fill="none" stroke="var(--red)" stroke-width="2"/></svg>
<div class="eyebrow" style="left:0;width:1200px;text-align:center;top:2068px;color:var(--blush)">Brisk Framing</div>
<h2 class="section-title" style="top:2080px;color:var(--white)">Recent Projects</h2>
<div class="recent-item" style="left:9px"><div class="ph" role="img" aria-label="Photo of a suburban house at dusk" style="background:linear-gradient(180deg,#6c7fc0,#c8b7c9)"></div><span>Project Name 1</span></div>
<div class="recent-item" style="left:247px"><div class="ph" role="img" aria-label="Photo of a modern brick facade" style="background:linear-gradient(135deg,#3a4048,#7a838c)"></div><span>Project Name 2</span></div>
<div class="recent-item" style="left:485px"><div class="ph" role="img" aria-label="Photo of a contemporary home with a garage" style="background:linear-gradient(180deg,#cfd3d6,#8d8a84)"></div><span>Project Name 3</span></div>
<div class="recent-item" style="left:723px"><div class="ph" role="img" aria-label="Photo of a modern interior with dining area" style="background:linear-gradient(135deg,#d8d6d2,#5a5a58)"></div><span>Project Name 4</span></div>
<div class="recent-item" style="left:962px"><div class="ph" role="img" aria-label="Photo of a white apartment building" style="background:linear-gradient(135deg,#e9ecef,#9fb0c4)"></div><span>Project Name 5</span></div>
<a class="btn btn-dark" style="left:529px;top:2391px;width:143px;height:31px">View More</a>

<div class="eyebrow" style="left:0;width:1200px;text-align:center;top:2575px;color:#777">What We Do</div>
<h2 class="section-title" style="top:2595px;color:var(--ink)">Our Services</h2>
<div class="service" style="left:116px">
  <svg width="60" height="56" viewBox="0 0 60 56" fill="none" stroke="var(--red)" stroke-width="2"><rect x="2" y="2" width="26" height="16"/><rect x="32" y="8" width="24" height="14"/><circle cx="16" cy="30" r="6"/><circle cx="44" cy="32" r="6"/><path d="M4 54v-6a12 12 0 0 1 24 0v6M32 54v-6a12 12 0 0 1 24 0v6"/></svg>
  <h3>Consultancy</h3>
  <p>Lorem ipsum dolor sit amet, consectetuer adipiscing elit, sed diam nonummy nibh euismod tincidunt ut laoreet dolore magna aliquam volutpat.</p>
</div>
<div class="service" style="left:368px">
  <svg width="78" height="56" viewBox="0 0 78 56" fill="none" stroke="var(--red)" stroke-width="2"><rect x="2" y="2" width="74" height="52"/><rect x="10" y="10" width="58" height="36"/><rect x="26" y="20" width="26" height="18"/><path d="M26 26h26M39 20v18"/></svg>
  <h3>Design</h3>
  <p>Ut wisi enim ad minim veniam, quis nostrud exerci tation ullamcorper suscipit lobortis nisl ut aliquip ex ea commodo consequat.</p>
</div>
<div class="service" style="left:620px">
  <svg width="58" height="58" viewBox="0 0 58 58" fill="none" stroke="var(--red)" stroke-width="2"><path d="M10 56V6h30M10 10h24M34 6v12"/><rect x="22" y="24" width="28" height="32"/><path d="M28 32h4M38 32h4M28 40h4M38 40h4M28 48h4M38 48h4M2 56h54"/></svg>
  <h3>Build</h3>
  <p>Duis autem vel eum iriure dolor in hendrerit in vulputate velit esse molestie vel illum dolore eu feugiat consequat.</p>
</div>
<div class="service" style="left:872px">
  <svg width="70" height="58" viewBox="0 0 70 58" fill="none" stroke="var(--red)" stroke-width="2"><path d="M2 24L20 6l18 18M8 18v18h24V18"/><circle cx="48" cy="24" r="9"/><path d="M37 20a11 11 0 0 1 22 0z"/><path d="M32 56v-8a16 16 0 0 1 32 0v8z"/></svg>
  <h3>Project Management</h3>
  <p>Dignissim qui blandit praesent luptatum zzril delenit augue duis dolore te feugait nulla facilisi.</p>
</div>

<div class="ph testimonials" role="img" aria-label="Faded photo of scaffolding behind client reviews"></div>
<svg class="abs" style="left:76px;top:3026px" width="84" height="36" viewBox="0 0 84 36"><polygon points="0,0 82,0 76,8 12,8 22,34 16,36" fill="var(--red)"/></svg>
<svg class="abs" style="left:596px;top:3026px" width="84" height="36" viewBox="0 0 84 36"><polygon points="0,0 82,0 76,8 12,8 22,34 16,36" fill="var(--red)"/></svg>
<blockquote class="testimonial" style="left:100px">
  <div class="qm">"</div>
  <div class="stars">★★★★★</div>
  <p>Duis autem vel eum iriure dolor in hendrerit in vulputate velit esse molestie consequat, vel illum dolore eu feugiat nulla facilisis at vero eros et accumsan et iusto odio dignissim.</p>
  <div class="who">- John D.</div>
</blockquote>
<blockquote class="testimonial" style="left:620px">
  <div class="qm">"</div>
  <div class="stars">★★★★★</div>
  <p>Lorem ipsum dolor sit amet, consectetuer adipiscing elit, sed diam nonummy nibh euismod tincidunt.</p>
  <div class="who">- Dave G.</div>
</blockquote>

<svg class="abs" style="left:0;top:3550px" width="1200" height="722" viewBox="0 3550 1200 722">
  <polygon points="0,3645 150,3620 1050,3557 1200,3600 1200,4272 0,4272" fill="#1f1f1f"/>
  <polygon points="150,3833 1050,3833 1050,3960 970,4025 150,3945" fill="var(--red)"/>
</svg>
<section class="contact-card">
  <svg class="chevron" style="left:435px;top:0" viewBox="0 0 30 22"><polygon points="0,0 30,0 15,22" fill="var(--red)"/><polyline points="9,6 15,12 21,6" fill="none" stroke="#fff" stroke-width="2"/></svg>
  <div class="eyebrow" style="left:0;width:900px;text-align:center;top:66px;color:#777">Get Connected</div>
  <h2 class="section-title" style="width:900px;top:82px;color:var(--ink)">Contact Us</h2>
  <div class="field" style="left:88px;top:163px;width:233px;height:31px">Name:</div>
  <div class="field" style="left:335px;top:163px;width:230px;height:31px">Phone:</div>
  <div class="field" style="left:579px;top:163px;width:229px;height:31px">Email:</div>
  <div class="field" style="left:88px;top:206px;width:720px;height:119px">Message / Questions:</div>
  <a class="btn btn-dark" style="left:379px;top:344px;width:143px;height:32px">Submit Form</a>
</section>
<div class="info" style="left:236px">
  <div class="tag"><svg width="12" height="12" viewBox="0 0 24 24" fill="none" stroke="#fff" stroke-width="2"><path d="M12 22s7-7 7-12a7 7 0 0 0-14 0c0 5 7 12 7 12z"/><circle cx="12" cy="10" r="2.5"/></svg></div>
  <small>location</small><span>Put Address Here, Put Address Here 123</span>
</div>
<div class="info" style="left:480px">
  <div class="tag"><svg width="12" height="12" viewBox="0 0 24 24" fill="none" stroke="#fff" stroke-width="2"><path d="M5 3h4l2 5-3 2a12 12 0 0 0 6 6l2-3 5 2v4a2 2 0 0 1-2 2A17 17 0 0 1 3 5a2 2 0 0 1 2-2z"/></svg></div>
  <small>phone</small><span style="font-size:18px">204-555-0193</span>
</div>
<div class="info" style="left:720px">
  <div class="tag"><svg width="12" height="12" viewBox="0 0 24 24" fill="none" stroke="#fff" stroke-width="2"><rect x="3" y="5" width="18" height="14"/><path d="M3 6l9 7 9-7"/></svg></div>
  <small>email</small><span>hello@briskframing.com</span>
</div>

<div class="brand" style="left:0;width:1200px;justify-content:center;top:4108px;font-size:40px"><span class="brand-mark" style="width:22px;height:22px"></span>Brisk Framing</div>
<div class="social">
  <span style="left:515px;top:4204px;background:#fff"></span>
  <span style="left:591px;top:4204px;background:#fff"></span>
  <span style="left:670px;top:4204px;background:#fff"></span>
</div>

<nav class="footer-nav">
  <a style="left:345px">HOME</a>
  <a style="left:442px">ABOUT</a>
  <a style="left:545px">SERVICES</a>
  <a style="left:665px">PROJECTS</a>
  <a style="left:786px">CONTACT US</a>
</nav>
<footer class="copyright">©2021. Brisk Framing. All Rights Reserved</footer>

</body>
</html>
```